The Garden Gate Circle website look (Wordpress)

We need a new website ~ wordpress design preferrably ~ to capture our personality .. unique and feminine, without being too girly or prissy! We are a business women's networking group which has been described as vibrant, rowdy and fun; a safe place for women to gather; holistic; and a little bit edgy. Unique and down to earth. Originally created by two close friends who met when their kids were in kindergarten together and out of a shared passion to encourage women to be more than a spectator to life; to create flexible, viable sources of income in order to allow more time for family, friends and other passions.
Our current website is: www.tggc.com.au
We have had a local designer working on our new website but are not satisfied:
http://www.craftventurepages.com/dev-sites/tggc/
Facebook page is: www.facebook.com/TGGC1
We are expanding and have branches in Cleveland, Coffs Harbour, Gold Coast and Springwood.
Inspiration sites: www.meadowlarkhaven.com (although background needs to be lighter!)
http://www.thebrightpathcollective.com (great content for a networking site but we need a little brighter).

Target Market(s)

Women aged between 30-50 juggling career and family. Fun, real, creative, vibrant, energetic, alive.

Industry/Entity Type

Business

Requirements
Must have
• Our colour scheme is pink and aqua (some bold; some pale .. see uploaded files for logo).
Two of our most often used taglines ~ and at least one of these should appear somewhere prominently so that page visitors can know right away what we do:
1. "A place for women to connect ~ business growth and personal development in a positive environment"
2. "The monthly event women DO look forward to.."
A feature of our website needs to be 'people' .. happy smiling faces and movement in a slider section (have uploaded some pics for inclusion but would like provision to add more).
Website must have provision for several tabs as there are many facets to our networking group. Must have a 'subscribe now for our top 10 networking tips' button (something a little funky :-) Must also have room somewhere for up to five major sponsor logos/advertising and a bold link to our forum.
One of the features of our group is the use of inspirational quotes .. we'll need to have a place on front page where quotes are displayed/alternated .. if you want an example, use "Well behaved women rarely make history" ~ Marion Delacourt Hayes
This is the first project I've listed so not sure how much detail to include re names of tabs etc.
Facebook and Pinterest tabs.
Nice to have
• Preferrably a white background but would like an impression or watermark image (possibly in very pale grey, pink or aqua) of a floral or scroll .. something that will tie in with the rest of the page.

Happy for you to surprise us with a design a little bit out of the square :-)
Should not have
• Should not be too 'kitchy' or too girly (the pics we've included have enough 'feminine' to carry that through, I think). The name of our company 'The Garden Gate Circle' refers to the concept of a Kitchen Table Entrepreneur and is aimed at a not-so-conservative, less formal, more open, honest and real woman, most likely a mother who is juggling both family and career.

```html
<!DOCTYPE html>
<html lang="en">
<head>
<meta charset="utf-8">
<title>The Garden Gate Circle</title>
<link href="https://fonts.googleapis.com/css2?family=PT+Sans:ital,wght@0,400;0,700;1,400&family=PT+Sans+Narrow:wght@700&display=swap" rel="stylesheet">
<style>
:root{
  --pink:#ec4a9c;
  --pink-light:#f7a8cf;
  --pink-pale:#f6c9de;
  --aqua:#1b9bb8;
  --aqua-bright:#27c4ea;
  --aqua-deep:#1479a0;
  --navy:#0f4f9a;
  --grey-text:#666;
  --grey-dark:#555;
  --footer-grey:#6d6c6e;
  --white:#fff;
}
*{margin:0;padding:0;box-sizing:border-box}
html,body{width:970px;height:1200px;overflow:hidden;background:var(--white)}
body{position:relative;font-family:"PT Sans",Arial,sans-serif;color:var(--grey-text)}
.abs{position:absolute}

/* header */
.brand{left:95px;top:34px;display:flex;align-items:center;gap:14px}
.brand-mark{width:56px;height:56px;background:var(--pink-light)}
.brand-name{font-weight:700;font-size:44px;color:var(--aqua);white-space:nowrap}
.search{left:686px;top:7px;width:188px;height:24px;border:1px solid #ccc;background:linear-gradient(#fff,#eee);display:flex}
.search span{flex:1;font-style:italic;font-size:12px;color:#aaa;padding:4px 8px}
.search b{width:39px;background:#555;color:#fff;font-size:11px;display:flex;align-items:center;justify-content:center}

/* main nav */
.main-nav{left:0;top:124px;width:970px;height:38px;background:linear-gradient(#f7a0c9,var(--pink) 55%,#e23d8f)}
.main-nav ul{list-style:none;position:absolute;left:0;top:0;width:970px;height:38px}
.main-nav li{position:absolute;top:0;color:#fff;font-size:11.5px;font-weight:700;line-height:38px;white-space:nowrap}
.main-nav li.active{background:linear-gradient(#5cc3dc,var(--aqua));padding:0 14px}
.social{left:748px;top:118px;display:flex;gap:3px}
.social i{width:26px;height:24px;display:block;border-radius:2px}

/* slider */
.slider-shadow{left:100px;top:400px;width:562px;height:62px;background:radial-gradient(ellipse at 50% 0,rgba(0,0,0,.18),transparent 70%)}
.slide{left:103px;top:175px;width:556px;height:232px;background:linear-gradient(120deg,#c9b39a,#8a6a5a 40%,#e9c1c6 70%,#b89a84)}
.slide-caption{left:100px;top:407px;width:562px;height:34px;background:#fff;border:1px solid #eee;border-top:none;font-family:"PT Sans Narrow",sans-serif;font-weight:700;font-size:19px;color:var(--grey-dark);text-align:center;line-height:30px}
.slide-arrow{top:276px}
.divider{left:100px;top:488px;width:562px;height:1px;background:#e8e8e8}

/* content */
.quote{left:103px;top:513px;width:556px;text-align:center;font-style:italic;font-size:14.5px;line-height:17.5px;color:var(--pink)}
.intro{left:103px;top:597px;width:560px;font-size:13px;line-height:15.5px;color:var(--grey-text)}
.intro p{margin-bottom:7px}
.section-title{left:103px;top:738px;font-family:"PT Sans Narrow",sans-serif;font-weight:700;font-size:25px;color:var(--pink)}
.partners{left:101px;top:774px;width:588px;height:184px;border:1px solid #ccc;border-radius:10px}
.partner-badge{position:absolute}

/* sidebar */
.login{left:687px;top:174px;width:173px;height:148px;border-radius:6px;background:linear-gradient(#1f6fc4,var(--navy));box-shadow:0 2px 3px rgba(0,0,0,.3)}
.login h3{color:#fff;font-weight:400;font-size:17px;padding:4px 11px}
.login-form{position:absolute;left:5px;top:33px;width:163px;height:110px;background:#fff;border-radius:5px;padding:10px 6px}
.login-form .field{height:19px;border:1px solid #ccc;background:#f1f1f1;font-size:12px;color:#999;padding:1px 6px;margin-bottom:5px}
.login-form .btn{display:inline-block;border:1px solid #ccc;background:linear-gradient(#fafafa,#e4e4e4);font-size:12px;color:#666;padding:1px 8px;margin-top:2px}
.login-form .links{display:flex;justify-content:space-between;font-size:9px;color:#333;margin-top:7px}
.login-form .links b{font-size:10px}
.news{left:682px;top:340px;width:187px;height:145px;border:1px solid #ccc;border-radius:3px;box-shadow:0 1px 3px rgba(0,0,0,.15)}
.news h3{font-size:13px;color:var(--pink);text-align:center;padding:6px 0 8px;background:linear-gradient(#fff,#f4f4f4);margin:0 8px}
.news p{font-size:11px;line-height:14px;color:var(--grey-dark);padding:0 10px 0 13px;margin-top:6px;margin-bottom:12px}
.subscribe{left:681px;top:506px;width:190px;height:190px;border-radius:50%;background:radial-gradient(circle,#c9c9c9 0 30%,#fff 31% 44%,var(--pink-pale) 45%,var(--pink-light) 100%)}
.affiliate{left:723px;top:718px;width:132px;height:263px;border:1px solid #ccc;background:#fff}
.affiliate h4{font-family:"PT Sans Narrow",sans-serif;font-weight:700;font-size:14px;line-height:18px;color:var(--aqua);text-align:center;padding-top:3px;height:40px;background:linear-gradient(#fff,#efefef)}
.affiliate-badge{position:absolute;left:8px;top:45px;width:115px;height:212px;background:#4f8d94}

/* footer */
.footer-nav{left:0;top:990px;width:970px;height:29px;background:var(--aqua)}
.footer-nav ul{list-style:none;display:flex;position:absolute;left:100px;top:0}
.footer-nav li{color:#fff;font-size:11.5px;font-weight:700;line-height:29px;margin-right:20px}
.footer{left:0;top:1019px;width:970px;height:181px;background:var(--footer-grey);font-family:Arial,sans-serif;color:#fff}
.footer h4{position:absolute;left:100px;top:14px;font-size:13px}
.contact-col{position:absolute;top:38px;font-size:11px;line-height:18.5px}
.legal{position:absolute;top:159px;font-size:11px}
</style>
</head>
<body>

<header>
  <div class="abs brand"><span class="brand-mark"></span><span class="brand-name">The Garden Gate Circle</span></div>
  <div class="abs search"><span>Search</span><b>Submit</b></div>
</header>

<nav class="abs main-nav">
  <ul>
    <li class="active" style="left:107px">Home</li>
    <li style="left:181px">Events</li>
    <li style="left:244px">Membership</li>
    <li style="left:336px">Directory</li>
    <li style="left:412px">Sponsorship</li>
    <li style="left:504px">Blog</li>
    <li style="left:557px">Contact</li>
  </ul>
</nav>
<div class="abs social" aria-label="Social links">
  <i style="background:#3b5a9a"></i><i style="background:#3fa9d9"></i><i style="background:#f08a24"></i><i style="background:#e9e9ef"></i>
</div>

<main>
  <div class="abs slider-shadow"></div>
  <div class="abs slide" role="img" aria-label="Photo of two smiling women seated at a table in a vintage-styled room"></div>
  <svg class="abs slide-arrow" style="left:110px" width="16" height="20" viewBox="0 0 16 20"><path d="M13 2 L4 10 L13 18" fill="none" stroke="#fff" stroke-width="3"/></svg>
  <svg class="abs slide-arrow" style="left:637px" width="16" height="20" viewBox="0 0 16 20"><path d="M3 2 L12 10 L3 18" fill="none" stroke="#fff" stroke-width="3"/></svg>
  <div class="abs slide-caption">A place for women to connect in a positive environment</div>
  <div class="abs divider"></div>

  <blockquote class="abs quote">“In the crazy struggle to juggle family, career and personal passions, women often forget to breathe. We forget about sunsets; sand between our toes; lazy Sundays in bed and the importance of being still!”</blockquote>

  <div class="abs intro">
    <p>Through effective networking and referrals amongst our expanding Membership; inspirational, motivational and educational guest speakers; and a constantly evolving growth platform,<br>The Garden Gate Circle seeks to offer opportunity, support and encouragement in a nurturing and positive environment.</p>
    <p>Whether individual needs are to spread the message of an established business; fire and grow a concept; or simply to enjoy like-minded company, we are committed to building a dynamic and vibrant community of women.</p>
  </div>

  <h2 class="abs section-title">Partners</h2>
  <div class="abs partners">
    <div class="partner-badge" style="left:9px;top:8px;width:136px;height:168px;background:#dfe6f0" role="img" aria-label="Blue Basin Planning partner badge"></div>
    <div class="partner-badge" style="left:166px;top:50px;width:414px;height:78px;background:#e6eef2" role="img" aria-label="Bayside Venture Hub partner badge"></div>
  </div>
</main>

<aside>
  <div class="abs login">
    <h3>Login</h3>
    <div class="login-form">
      <div class="field">username</div>
      <div class="field">password</div>
      <span class="btn">Login</span>
      <div class="links"><span>Forgot your password?</span><b>Sign Up</b></div>
    </div>
  </div>

  <div class="abs news">
    <h3>Latest News</h3>
    <p>Natus fermentum Natus fermnum, aliquid molestiae magnis? Quas? Phasellus donec?</p>
    <p>Vestibulum maecenas sollicitudin arcu?</p>
  </div>

  <div class="abs subscribe" role="img" aria-label="Subscribe button: subscribe to receive our top ten networking tips"></div>

  <div class="abs affiliate">
    <h4>Proudly affiliated with:<br>The Nest Branch</h4>
    <div class="affiliate-badge" role="img" aria-label="The Nest Branch affiliate badge"></div>
  </div>
</aside>

<nav class="abs footer-nav">
  <ul><li>Home</li><li>Events</li><li>Membership</li><li>Directory</li><li>Sponsorship</li><li>Blog</li><li>Contact Us</li></ul>
</nav>

<footer class="abs footer">
  <h4>Contact Us</h4>
  <div class="contact-col" style="left:100px">Clara Wyndham<br>Lot 9 Fernhill Road<br>Ashbourne, SA, 5157<br>PO Box 482<br>Ashbourne, SA, 5157</div>
  <div class="contact-col" style="left:224px">Phone Work/Mobile: 0400 555 123<br>Phone: 08 5550 1234<br>Fax: 08 5550 1299<br>Email: clara@fernhillgardens.com</div>
  <svg class="abs" style="left:688px;top:9px" width="136" height="136" viewBox="0 0 136 136" aria-label="Join now">
    <circle cx="68" cy="68" r="64" fill="var(--aqua-bright)"/>
    <circle cx="68" cy="68" r="55" fill="var(--footer-grey)"/>
    <circle cx="68" cy="68" r="50" fill="var(--aqua-bright)"/>
    <text x="68" y="62" text-anchor="middle" font-family="PT Sans Narrow,sans-serif" font-weight="700" font-size="28" fill="var(--aqua-deep)" transform="rotate(-18 68 68)">JOIN</text>
    <text x="68" y="92" text-anchor="middle" font-family="PT Sans Narrow,sans-serif" font-weight="700" font-size="28" fill="var(--aqua-deep)" transform="rotate(-18 68 68)">NOW</text>
  </svg>
  <div class="legal" style="left:100px">© 2009-2012 The Garden Gate Circle, All rights reserved.</div>
  <div class="legal" style="left:607px">Disclaimer &nbsp;|&nbsp; Privacy policy &nbsp;|&nbsp; Hiring &nbsp;|&nbsp; SiteMap</div>
</footer>

</body>
</html>
```